Coral Ridge Pools New website

I currently operate a swimming pool service and repair business and looking for a re design for my website as it has been over 5 years since it was designed. current site is coralridgepoolsqx.com

```html
<!DOCTYPE html>
<html lang="en">
<head>
<meta charset="utf-8">
<title>Coral Ridge Pools QX</title>
<link href="https://fonts.googleapis.com/css2?family=Poppins:wght@400;500;600;700&display=swap" rel="stylesheet">
<style>
:root{
  --stage:#ababab;
  --navy:#0b2545;
  --ink:#2b3340;
  --brand-blue:#005a9c;
  --orange:#ff8a00;
  --soft-bg:#f6f8fd;
  --white:#ffffff;
  --nav-bg:rgba(240,242,247,0.95);
  --footer:#00213f;
  --line:#cfd5de;
  --hero-top:#3b4470;
  --hero-bottom:#2a55b8;
  --photo-top:#5d6785;
  --photo-bottom:#3567c4;
}
*{box-sizing:border-box;margin:0;padding:0}
html,body{width:1200px;height:2688px;overflow:hidden}
body{background:var(--stage);font-family:'Poppins',sans-serif;color:var(--ink);position:relative}
.page{position:absolute;left:112px;top:107px;width:977px;height:2474px;background:var(--white);box-shadow:0 4px 18px rgba(0,0,0,0.25);overflow:hidden}
.wrap{width:732px;margin:0 auto}

/* header */
.site-header{position:absolute;left:0;top:0;width:100%;height:50px;background:var(--nav-bg);z-index:3;display:flex;align-items:center;justify-content:space-between;padding:0 128px 0 104px}
.brand{display:flex;align-items:center;gap:8px;font-size:14px;font-weight:600;color:var(--brand-blue)}
.brand-dot{width:14px;height:14px;border-radius:50%;background:var(--orange)}
.main-nav{display:flex;gap:27px;font-size:11.5px;font-weight:500;color:var(--navy)}

/* hero */
.hero{position:absolute;left:0;top:0;width:100%;height:662px;clip-path:polygon(0 0,100% 0,100% 95.5%,0 100%)}
.hero-photo{position:absolute;inset:0;background:linear-gradient(180deg,var(--hero-top) 0%,var(--hero-bottom) 100%)}
.hero-content{position:absolute;top:296px;left:0;width:100%;text-align:center;color:var(--white);z-index:1}
.hero-title{font-size:31px;font-weight:700;letter-spacing:-0.3px;line-height:40px}
.hero-sub{font-size:13px;line-height:20px;margin:12px auto 0;width:340px}
.btn{display:inline-block;background:var(--orange);color:var(--white);font-weight:600;border-radius:20px}
.hero .btn{margin-top:17px;font-size:11px;padding:9px 17px}

/* services */
.services{position:absolute;top:662px;left:0;width:100%;height:340px;background:var(--white)}
.section-title{font-size:24px;font-weight:700;color:var(--navy);text-align:center}
.services .section-title{margin-top:61px}
.service-grid{display:flex;gap:20px;margin-top:42px}
.service-card{width:168px;height:173px;background:var(--white);border-radius:6px;box-shadow:0 2px 8px rgba(11,37,69,0.08);text-align:center;padding:20px 18px 0}
.service-card h3{font-size:13.5px;font-weight:600;color:var(--navy);line-height:21px}
.service-card p{font-size:10.5px;line-height:16px;margin-top:8px;color:var(--ink)}

/* about */
.about{position:absolute;top:1002px;left:0;width:100%;height:677px;background:var(--soft-bg)}
.about .section-title{margin-top:55px}
.about-text{margin-top:28px;font-size:11px;line-height:17px;color:var(--ink)}
.about-text p+p{margin-top:11px}
.btn-blue{background:var(--brand-blue);font-size:11px;padding:7px 13px;margin-top:11px}
.about-photo{margin-top:21px;width:531px;height:354px;border-radius:6px;background:linear-gradient(180deg,var(--photo-top) 0%,var(--photo-bottom) 100%)}

/* call to action */
.cta{position:absolute;top:1679px;left:0;width:100%;height:216px;background:var(--brand-blue);text-align:center}
.cta h2{margin-top:57px;font-size:21px;font-weight:700;color:var(--navy)}
.cta p{font-size:12px;color:var(--white);margin-top:10px}
.cta .btn{margin-top:18px;font-size:11px;padding:9px 16px}

/* contact */
.contact{position:absolute;top:1895px;left:0;width:100%;height:495px;background:var(--soft-bg)}
.contact .section-title{margin-top:58px}
.contact-lead{text-align:center;font-size:11px;margin-top:16px;color:var(--ink)}
.contact-body{display:flex;margin-top:26px;align-items:flex-start}
.contact-form{width:409px;height:291px;background:var(--white);border-radius:6px;box-shadow:0 2px 8px rgba(11,37,69,0.06);padding:21px 21px 0}
.field{width:367px;height:32px;border:1px solid var(--line);border-radius:3px;font-size:10.5px;color:#6a717c;padding:8px 9px;margin-bottom:11px;background:var(--white)}
.field-area{height:78px}
.contact-form .btn{font-size:9.5px;padding:6px 16px;margin-top:2px}
.contact-info{margin-left:32px;margin-top:84px}
.contact-info h4{font-size:12.5px;font-weight:600;color:var(--navy)}
.contact-info ul{list-style:none;margin-top:10px;padding-left:5px;font-size:10.5px;line-height:22px;color:var(--ink)}

/* footer */
.site-footer{position:absolute;top:2390px;left:0;width:100%;height:84px;background:var(--footer);color:var(--white);text-align:center;font-size:10px;line-height:21px;padding-top:21px}
</style>
</head>
<body>
<div class="page">
  <header class="site-header">
    <div class="brand"><span class="brand-dot"></span>Coral Ridge Pools</div>
    <nav class="main-nav"><span>Home</span><span>Services</span><span>About</span><span>Contact</span></nav>
  </header>

  <section class="hero">
    <div class="hero-photo" role="img" aria-label="Photo of a rooftop swimming pool at dusk"></div>
    <div class="hero-content">
      <h1 class="hero-title">Crystal Clear Pools, All Year Round</h1>
      <p class="hero-sub">Your trusted partner for pool maintenance, repair &amp; remodeling in Harbor Vale.</p>
      <span class="btn">Get a Free Quote</span>
    </div>
  </section>

  <section class="services">
    <h2 class="section-title">Our Services</h2>
    <div class="wrap service-grid">
      <div class="service-card"><h3>Pool Cleaning</h3><p>Regular cleaning to keep your pool sparkling clean &amp; hygienic for your family and friends.</p></div>
      <div class="service-card"><h3>Repairs &amp; Equipment</h3><p>From leak detection to pump &amp; filter repairs, our technicians fix issues promptly &amp; professionally.</p></div>
      <div class="service-card"><h3>Maintenance Plans</h3><p>Custom maintenance plans tailored to your needs for worry-free pool ownership.</p></div>
      <div class="service-card"><h3>Renovation &amp; Remodel</h3><p>Transform your backyard with custom pool resurfacing, tile work &amp; modern upgrades.</p></div>
    </div>
  </section>

  <section class="about">
    <h2 class="section-title">About Coral Ridge Pools QX</h2>
    <div class="wrap">
      <div class="about-text">
        <p>Coral Ridge Pools QX is a family-owned and operated pool service and repair company serving Harbor Vale and surrounding areas. With over a decade of experience, we are dedicated to providing reliable, top-quality pool care so you can enjoy your backyard oasis year round.</p>
        <p>We take pride in our attention to detail, friendly customer service, and deep knowledge of pool systems. Whether you need weekly cleaning, urgent repairs or a complete pool renovation, our certified technicians are here to help.</p>
      </div>
      <span class="btn btn-blue">Learn More</span>
      <div class="about-photo" role="img" aria-label="Photo of a rooftop pool with lounge chairs at sunset"></div>
    </div>
  </section>

  <section class="cta">
    <h2>Relax, We’ve Got Your Pool Covered</h2>
    <p>Let our experts keep your pool safe, clean &amp; ready for every occasion.</p>
    <span class="btn">Schedule Service</span>
  </section>

  <section class="contact">
    <h2 class="section-title">Contact Us</h2>
    <p class="contact-lead">Ready to make a splash? Send us a message or give us a call and we’ll get back to you as soon as possible.</p>
    <div class="wrap contact-body">
      <div class="contact-form">
        <div class="field">Your Name</div>
        <div class="field">Email Address</div>
        <div class="field">Phone Number</div>
        <div class="field field-area">How can we help you?</div>
        <span class="btn">Send Message</span>
      </div>
      <div class="contact-info">
        <h4>Get in Touch</h4>
        <ul>
          <li>(555) 014-2290</li>
          <li>info@coralridgepoolsqx.com</li>
          <li>Harbor Vale, QX</li>
        </ul>
      </div>
    </div>
  </section>

  <footer class="site-footer">
    <p>© 2026 Coral Ridge Pools QX. All rights reserved.</p>
    <p>Designed by Our Web Team.</p>
  </footer>
</div>
</body>
</html>
```